Soccer (Football) travel website

I need a responsive 1-page website design for a vacation/trip review website, plus a basic logo. The site's name is GlobalPitchJourneys.com.

A site I have in mind is HarborVerdict.com:

https://www.harborverdict.example/sailto/sailroutes.cfm?port=149&startDate=2019-08

Target Market(s)

Landing page used to attract people after they've clicked on an advertisement

Industry/Entity Type

Travel

Logo Text

GlobalPitchJourneys.com

Number of Pages Required

1 page

Font styles to use
Sans Serif

Colors

Designer to choose colors to be used in the design.

Requirements
Must have
• A header that takes up very little vertical space.
• I've attached one file. This is what the content will consist of in the center of the site: a photo of a stadium with some description text below it.
Nice to have
• Needs to have a simple nav plus links for social media and newsletter

```html
<!DOCTYPE html>
<html lang="en">
<head>
<meta charset="utf-8">
<title>GlobalPitchJourneys.com</title>
<link href="https://fonts.googleapis.com/css2?family=Roboto:wght@400;500;700&family=Permanent+Marker&display=swap" rel="stylesheet">
<style>
:root{
  --ink:#1b1b1f;
  --sidebar:#18181c;
  --navy:#1c1b2c;
  --footer:#1d1b3d;
  --red:#d7262f;
  --gold:#f6c21b;
  --white:#ffffff;
  --muted:#555;
  --panel:#d6d6d6;
}
*{box-sizing:border-box;margin:0;padding:0}
html,body{width:1200px;height:3547px;overflow:hidden}
body{position:relative;font-family:'Roboto',Arial,sans-serif;color:var(--ink);background:var(--white)}
.abs{position:absolute}
/* sidebar */
.sidebar{position:absolute;left:0;top:0;width:75px;height:3235px;background:var(--sidebar);z-index:5}
.burger{position:absolute;left:22px;top:22px;width:30px}
.burger span{display:block;height:3px;background:var(--white);margin-bottom:7px}
.brand-mark{position:absolute;left:9px;top:66px;width:56px;height:56px;border:3px solid var(--white);border-radius:50%}
.brand-name{position:absolute;left:29px;top:136px;writing-mode:vertical-rl;color:var(--white);font-size:11px;font-weight:500;letter-spacing:1px}
.social-dot{position:absolute;left:28px;width:18px;height:18px;border-radius:50%;background:var(--white)}
.side-label{position:absolute;left:28px;writing-mode:vertical-rl;transform:rotate(180deg);color:var(--white);font-size:13px;letter-spacing:1px;border-top:1px solid var(--white);padding-top:6px}
/* hero */
.hero{position:absolute;left:75px;top:0;width:1125px;height:625px;background:linear-gradient(180deg,#0d2f5c 0%,#143d6e 35%,#1f5a2a 70%,#2f8a2c 100%)}
.hero-title{position:absolute;left:74px;top:170px;font-family:'Permanent Marker','Brush Script MT','Segoe Script',cursive;font-weight:400;color:var(--white);font-size:84px;line-height:1.25;letter-spacing:1px}
.hero-title .line2{display:block;padding-left:80px}
.btn{display:flex;align-items:center;justify-content:center;font-size:12px;font-weight:500;letter-spacing:1px;text-transform:uppercase}
.btn-light{background:var(--white);color:var(--ink);border:1px solid #999}
.btn-outline-dark{border:1px solid #888;color:var(--ink);background:var(--white)}
.btn-outline-light{border:2px solid var(--white);color:var(--white)}
.btn-dark{background:var(--ink);color:var(--white)}
/* about */
.section-heading{font-size:31px;font-weight:700;letter-spacing:2px;text-transform:uppercase}
.section-heading span{border-bottom:2px solid currentColor}
.body-copy{font-size:12.5px;line-height:1.78;color:#333}
.photo{position:absolute}
.dots{position:absolute;left:1160px;width:8px}
.dots i{display:block;width:7px;height:7px;border-radius:50%;border:1px solid #bbb;margin-bottom:6px}
.dots i.on{background:var(--red);border-color:var(--red)}
/* featured */
.featured{position:absolute;left:75px;top:1407px;width:1125px;height:649px;background:var(--navy);color:var(--white)}
.centered-title{position:absolute;left:0;width:100%;text-align:center}
.meta{font-size:22px;font-weight:500;letter-spacing:1px;text-transform:uppercase}
.meta em{font-style:normal;color:var(--red)}
/* tours */
.tour-info p{font-size:16px;margin-bottom:26px}
.tour-info p em{font-style:normal;color:var(--red)}
.reviews{font-size:17px}
.learn{font-size:17px;display:flex;align-items:center;gap:10px}
.learn span{border-bottom:1px solid var(--ink)}
.filters{position:absolute;left:861px;top:2203px;width:190px;height:546px;background:var(--panel);border:2px solid #999;padding:14px 22px;font-size:11px}
.filters h3{color:var(--red);font-size:19px;font-weight:700;margin-bottom:12px}
.filters h4{color:var(--red);font-size:16px;font-weight:700;margin:14px 0 8px}
.check{display:flex;align-items:center;gap:6px;margin-bottom:6px}
.box{width:12px;height:12px;border:1px solid #444;background:var(--white);display:inline-block}
.box.on{background:#444;box-shadow:inset 0 0 0 2px var(--white)}
.month-row{display:flex;gap:7px;margin-bottom:4px}
.month-row span{width:12px;text-align:center}
/* footer */
.footer{position:absolute;left:75px;top:3235px;width:1125px;height:312px;background:var(--footer);color:var(--white)}
.footer h5{font-size:12px;font-weight:700;letter-spacing:1px;text-transform:uppercase}
.footer li{list-style:none;font-size:11px;margin-bottom:10px}
.footer small{font-size:11px}
</style>
</head>
<body>

<aside class="sidebar">
  <div class="burger"><span></span><span></span><span></span></div>
  <div class="brand-mark"></div>
  <div class="brand-name">GlobalPitchJourneys</div>
  <div class="social-dot" style="top:398px"></div>
  <div class="social-dot" style="top:424px"></div>
  <div class="social-dot" style="top:450px"></div>
  <div class="side-label" style="top:490px">Follow Us</div>
  <div class="side-label" style="top:980px">ABOUT US</div>
  <div class="side-label" style="top:1700px">FEATURED</div>
  <div class="side-label" style="top:2370px">TOURS</div>
</aside>

<header class="hero" role="img" aria-label="Night stadium with a player's boot resting on a football on the pitch">
  <h1 class="hero-title">WANT TO WATCH<span class="line2">THIS CLOSE ?</span></h1>
  <a class="btn btn-light abs" style="left:228px;top:440px;width:173px;height:48px">Join Us</a>
</header>

<section class="about">
  <h2 class="section-heading abs" style="left:149px;top:715px"><span>Who we are?</span></h2>
  <p class="body-copy abs" style="left:149px;top:770px;width:390px">Global Pitch Journeys is Lorem ipsum dolor sit amet, consectetur adipiscing elit, sed do eiusmod tempor incididunt ut labore et dolore magna aliqua. Ut enim ad minim veniam, quis nostrud exercitation ullamco laboris nisi ut aliquip ex ea commodo consequat. eiusmod tempor incididunt ut labore et dolore magna aliqua.</p>
  <div class="photo" style="left:637px;top:688px;width:375px;height:250px;background:linear-gradient(135deg,#e8c21a,#f4d83a 50%,#b89410)" role="img" aria-label="Fan holding a yellow smoke flare"></div>

  <div class="photo" style="left:149px;top:1000px;width:452px;height:282px;background:linear-gradient(180deg,#f4a53c,#e4612a 55%,#5a2312)" role="img" aria-label="Silhouette kicking a ball against a sunset"></div>
  <h2 class="section-heading abs" style="left:637px;top:1045px"><span>Why travel with us?</span></h2>
  <p class="body-copy abs" style="left:637px;top:1098px;width:390px">Global Pitch Journeys is Lorem ipsum dolor sit amet, consectetur adipiscing elit, sed do eiusmod tempor incididunt ut labore et dolore magna aliqua. Ut enim ad minim veniam, quis nostrud exercitation ullamco laboris nisi ut aliquip ex ea commodo consequat. eiusmod tempor incididunt ut labore et dolore magna aliqua.</p>
  <a class="btn btn-outline-dark abs" style="left:724px;top:1294px;width:178px;height:48px">Join Us</a>
  <div class="dots" style="top:995px"><i class="on"></i><i></i><i></i></div>
</section>

<section class="featured">
  <h2 class="section-heading centered-title" style="top:55px;font-weight:500"><span>Our featured tours</span></h2>
  <div class="photo" style="left:156px;top:138px;width:813px;height:280px;background:linear-gradient(180deg,#5d86b8,#3a5d8a)" role="img" aria-label="Neighbouring stadium slides"></div>
  <div class="photo" style="left:187px;top:113px;width:750px;height:315px;background:linear-gradient(180deg,#8fb4dd 0%,#b5cbe0 30%,#c8202c 45%,#a8151f 65%,#3f8a37 80%,#2e7a2c 100%)" role="img" aria-label="Stadium with red stands and green pitch"></div>
  <svg class="abs" style="left:92px;top:245px" width="30" height="50" viewBox="0 0 30 50"><path d="M25 4 L6 25 L25 46" fill="none" stroke="var(--red)" stroke-width="7"/></svg>
  <svg class="abs" style="left:997px;top:245px" width="30" height="50" viewBox="0 0 30 50"><path d="M5 4 L24 25 L5 46" fill="none" stroke="var(--white)" stroke-width="7"/></svg>
  <p class="meta abs" style="left:339px;top:485px">Place: <em>Liverpool</em></p>
  <p class="meta abs" style="left:622px;top:485px">Date: <em>March</em></p>
  <a class="btn btn-outline-light abs" style="left:372px;top:539px;width:140px;height:48px">Read More</a>
  <a class="btn btn-light abs" style="left:579px;top:539px;width:173px;height:48px">Travel Now</a>
  <div class="dots" style="left:1087px;top:350px"><i></i><i class="on"></i><i></i></div>
</section>

<section class="tours">
  <h2 class="section-heading abs" style="left:75px;width:1125px;text-align:center;top:2110px;font-weight:500;letter-spacing:2px">Pick a tour now</h2>

  <svg width="0" height="0" style="position:absolute"><defs>
    <polygon id="star" points="10,1 12.6,7 19,7.4 14,11.6 15.6,18 10,14.5 4.4,18 6,11.6 1,7.4 7.4,7" fill="var(--gold)"/>
    <clipPath id="half"><rect x="0" y="0" width="10" height="20"/></clipPath>
  </defs></svg>

  <div class="photo" style="left:149px;top:2203px;width:250px;height:217px;background:linear-gradient(180deg,#c9b8a8,#8b8f92 55%,#3d6b34)" role="img" aria-label="Stadium at dusk"></div>
  <div class="tour-info abs" style="left:430px;top:2230px"><p>Place: <em>Liverpool</em></p><p>Date: <em>25th March</em></p><p>Duration: <em>3 weeks</em></p><p>Price Range: <em>$2000 - $2700</em></p></div>
  <svg class="abs" style="left:693px;top:2222px" width="110" height="20"><use href="#star"/><use href="#star" x="22"/><use href="#star" x="44"/><use href="#star" x="66"/><use href="#star" x="88"/></svg>
  <p class="reviews abs" style="left:693px;top:2277px">(3245 reviews)</p>
  <p class="learn abs" style="left:693px;top:2320px"><span>Learn more</span><svg width="34" height="10"><path d="M0 5H30M25 1L31 5L25 9" stroke="var(--ink)" stroke-width="2" fill="none"/></svg></p>
  <a class="btn btn-dark abs" style="left:693px;top:2371px;width:139px;height:49px">Book Now</a>

  <div class="photo" style="left:149px;top:2453px;width:250px;height:217px;background:linear-gradient(180deg,#d6e3ee,#9ca4aa 50%,#4a4d4f)" role="img" aria-label="Empty stadium with grey seats"></div>
  <div class="tour-info abs" style="left:430px;top:2480px"><p>Place: <em>London</em></p><p>Date: <em>21st October</em></p><p>Duration: <em>2 weeks</em></p><p>Price Range: <em>$2000 - $5000</em></p></div>
  <svg class="abs" style="left:693px;top:2472px" width="110" height="20"><use href="#star"/><use href="#star" x="22"/><use href="#star" x="44"/><use href="#star" x="66"/><use href="#star" x="88" clip-path="url(#half)"/></svg>
  <p class="reviews abs" style="left:693px;top:2527px">(467 reviews)</p>
  <p class="learn abs" style="left:693px;top:2570px"><span>Learn more</span><svg width="34" height="10"><path d="M0 5H30M25 1L31 5L25 9" stroke="var(--ink)" stroke-width="2" fill="none"/></svg></p>
  <a class="btn btn-dark abs" style="left:693px;top:2621px;width:139px;height:49px">Book Now</a>

  <div class="photo" style="left:149px;top:2703px;width:250px;height:217px;background:linear-gradient(180deg,#1a1d24,#3a3f46 50%,#2c5a2a)" role="img" aria-label="Floodlit stadium at night with crowd"></div>
  <div class="tour-info abs" style="left:430px;top:2730px"><p>Place: <em>Manchester</em></p><p>Date: <em>12th February</em></p><p>Duration: <em>4 weeks</em></p><p>Price Range: <em>$1500 - $2350</em></p></div>
  <svg class="abs" style="left:693px;top:2722px" width="110" height="20"><use href="#star"/><use href="#star" x="22"/><use href="#star" x="44"/><use href="#star" x="66"/><use href="#star" x="88" clip-path="url(#half)"/></svg>
  <p class="reviews abs" style="left:693px;top:2777px">(99 reviews)</p>
  <p class="learn abs" style="left:693px;top:2820px"><span>Learn more</span><svg width="34" height="10"><path d="M0 5H30M25 1L31 5L25 9" stroke="var(--ink)" stroke-width="2" fill="none"/></svg></p>
  <a class="btn btn-dark abs" style="left:693px;top:2871px;width:139px;height:49px">Book Now</a>

  <div class="photo" style="left:149px;top:2953px;width:250px;height:217px;background:linear-gradient(180deg,#20232b,#4b4f5a 45%,#3f7a36)" role="img" aria-label="Covered stadium interior with lit pitch"></div>
  <div class="tour-info abs" style="left:430px;top:2980px"><p>Place: <em>Chelsea</em></p><p>Date: <em>3rd June</em></p><p>Duration: <em>1 week</em></p><p>Price Range: <em>$1000 - $1900</em></p></div>
  <svg class="abs" style="left:693px;top:2972px" width="110" height="20"><use href="#star"/><use href="#star" x="22"/><use href="#star" x="44"/><use href="#star" x="66"/><use href="#star" x="88"/></svg>
  <p class="reviews abs" style="left:693px;top:3027px">(32415 reviews)</p>
  <p class="learn abs" style="left:693px;top:3070px"><span>Learn more</span><svg width="34" height="10"><path d="M0 5H30M25 1L31 5L25 9" stroke="var(--ink)" stroke-width="2" fill="none"/></svg></p>
  <a class="btn btn-dark abs" style="left:693px;top:3121px;width:139px;height:49px">Book Now</a>

  <aside class="filters">
    <h3>FILTERS</h3>
    <h4 style="margin-top:0">Destination</h4>
    <div class="check"><span class="box on"></span>Amsterdam</div>
    <div class="check"><span class="box"></span>Berlin</div>
    <div class="check"><span class="box"></span>Congo</div>
    <div class="check"><span class="box"></span>Dubai</div>
    <div class="check"><span class="box"></span>Moscow</div>
    <h4>Month</h4>
    <div class="month-row"><span>1</span><span>2</span><span>3</span><span>4</span><span>5</span><span>6</span></div>
    <div class="month-row"><span class="box on"></span><span class="box on"></span><span class="box"></span><span class="box"></span><span class="box"></span><span class="box"></span></div>
    <div class="month-row" style="margin-top:8px"><span>7</span><span>8</span><span>9</span><span>10</span><span>11</span><span>12</span></div>
    <div class="month-row"><span class="box on"></span><span class="box on"></span><span class="box"></span><span class="box"></span><span class="box"></span><span class="box"></span></div>
    <h4>Price</h4>
    <div style="display:flex;justify-content:space-between"><span>$0</span><span>$5000+</span></div>
    <svg width="142" height="16"><line x1="5" y1="8" x2="137" y2="8" stroke="var(--red)" stroke-width="3"/><circle cx="6" cy="8" r="6" fill="var(--red)"/><circle cx="136" cy="8" r="6" fill="var(--red)"/></svg>
    <h4>Duration</h4>
    <div style="display:flex;align-items:center;gap:10px"><span style="background:var(--ink);color:var(--white);padding:6px 8px;border-radius:3px;font-size:12px">12 ▾</span><span>Days</span></div>
  </aside>
  <div class="dots" style="top:2372px"><i></i><i></i><i class="on"></i></div>
</section>

<footer class="footer">
  <svg class="abs" style="left:547px;top:-15px" width="30" height="30"><circle cx="15" cy="15" r="15" fill="var(--red)"/><path d="M8 12L15 19L22 12" stroke="var(--white)" stroke-width="3" fill="none"/></svg>
  <div class="abs" style="left:74px;top:62px">
    <h5>Site Map</h5>
    <ul style="margin-top:18px"><li>Home</li><li>About Us</li><li>Tours</li><li>Featured Trips</li></ul>
  </div>
  <div class="abs" style="left:230px;top:62px;width:1px;height:165px;background:#6a6a86"></div>
  <div class="abs" style="left:327px;top:62px">
    <h5>Follow Us</h5>
    <div style="display:flex;gap:10px;margin-top:18px"><span style="width:18px;height:18px;border-radius:50%;background:var(--white)"></span><span style="width:18px;height:18px;border-radius:50%;background:var(--white)"></span><span style="width:18px;height:18px;border-radius:50%;background:var(--white)"></span></div>
    <div style="width:186px;height:1px;background:#6a6a86;margin:20px 0 18px"></div>
    <h5>Contact Us</h5>
    <p style="margin-top:16px"><small>Phone: +1 800 555 0142</small></p>
    <p style="margin-top:10px"><small>Email: info@globalpitchjourneys.com</small></p>
  </div>
  <div class="abs" style="left:608px;top:62px">
    <h5>Subscribe to our newsletter</h5>
    <div style="margin-top:16px;width:219px;height:37px;background:var(--white);border-radius:3px;color:#999;font-size:11px;padding:12px 10px">Your Email</div>
    <div class="btn" style="margin-top:21px;width:125px;height:34px;border:1px solid var(--white);font-size:11px">Subscribe</div>
  </div>
  <div class="abs" style="left:880px;top:148px;display:flex;align-items:center;gap:8px">
    <span style="width:56px;height:56px;border-radius:50%;border:3px solid var(--white)"></span>
    <span style="font-size:12px;font-weight:700">GlobalPitchJourneys</span>
  </div>
  <div class="abs" style="left:74px;top:248px;width:128px;height:1px;background:#6a6a86"></div>
  <p class="abs" style="left:74px;top:274px"><small>Privacy Policy &nbsp;&nbsp;|&nbsp;&nbsp; Terms and Conditions</small></p>
</footer>

</body>
</html>
```